Need a flyer to leave behind when visiting clients or at shows

Glossy colorful tri-fold flyer with the same information that is on my web site www.brevalinkpro.com. I am open to a little modern or creative take on the typical brochure. I created the web site so I can provide any raw files needed from it. I would also like the ability to edit this flyer in the future in Adobe Photoshop Elements

```html
<!DOCTYPE html>
<html lang="en">
<head>
<meta charset="utf-8">
<title>Brevalink Pro — IT Expertise for Post-Acute Care</title>
<link rel="stylesheet" href="https://fonts.googleapis.com/css2?family=Montserrat:wght@400;500;700&family=Source+Serif+4:wght@400&display=swap">
<style>
  :root {
    --purple: #6a44a0;
    --ink: #1f3b57;
    --gold: #f1dfae;
    --white: #ffffff;
    --body-font: "Source Serif 4", Georgia, serif;
    --head-font: "Montserrat", Arial, sans-serif;
  }
  * { margin: 0; padding: 0; box-sizing: border-box; }
  html, body { width: 1200px; height: 927px; overflow: hidden; background: var(--white); }
  .flyer { position: relative; width: 1200px; height: 927px; font-family: var(--body-font); color: var(--ink); }
  .block { position: absolute; }

  .photo-meeting { left: 0; top: 0; width: 398px; height: 350px;
    background: linear-gradient(135deg, #c9c2b6 0%, #e6e1d8 45%, #a9a49b 100%); }
  .photo-medical { left: 400px; top: 350px; width: 800px; height: 320px;
    background: linear-gradient(100deg, #eef3f8 0%, #dbe7f2 35%, #b9cfe2 65%, #e4edf5 100%); }
  .photo-desk { left: 800px; top: 670px; width: 400px; height: 257px;
    background: linear-gradient(160deg, #e9d9cf 0%, #f5efe9 45%, #d8dde2 100%); }

  .headline-panel { left: 398px; top: 0; width: 402px; height: 350px; background: var(--white); }
  .headline { position: absolute; left: 31px; top: 38px; width: 360px;
    font-family: var(--head-font); font-weight: 500; font-size: 29px; line-height: 50px;
    letter-spacing: 1.6px; color: var(--ink); }

  .values-panel { left: 800px; top: 0; width: 400px; height: 350px; background: var(--purple); color: var(--white); }
  .label { font-family: var(--head-font); font-weight: 700; font-size: 13px; letter-spacing: 2.8px; color: var(--gold); text-transform: uppercase; }
  .values-panel .label { position: absolute; left: 38px; }
  .values-panel ul { position: absolute; left: 38px; list-style: none; font-size: 16px; }
  .label-values { top: 36px; }
  .list-values { top: 64px; line-height: 24px; }
  .label-objectives { top: 191px; }
  .list-objectives { top: 225px; line-height: 26.5px; width: 340px; }

  .services-panel { left: 0; top: 350px; width: 400px; height: 577px; background: var(--purple); color: var(--white); }
  .services-title { position: absolute; left: 39px; top: 28px; font-family: var(--head-font); font-weight: 700;
    font-size: 38px; line-height: 46px; letter-spacing: 3.5px; }
  .services-intro { position: absolute; left: 39px; top: 147px; width: 328px; font-size: 15.5px; line-height: 24px; }
  .services-panel .label { position: absolute; left: 39px; top: 367px; }
  .it-list { position: absolute; left: 39px; top: 395px; list-style: none; font-size: 16px; line-height: 26px; letter-spacing: 0.5px; }

  .mission-panel { left: 400px; top: 670px; width: 400px; height: 257px; background: var(--white); }
  .statement { position: absolute; left: 29px; width: 340px; font-size: 16.5px; line-height: 24px; }
  .statement-mission { top: 12px; }
  .statement-goal { top: 132px; }
</style>
</head>
<body>
<main class="flyer">
  <div class="block photo-meeting" role="img" aria-label="Photo of business people meeting and talking in a bright office"></div>

  <section class="block headline-panel">
    <h1 class="headline">Providing Information Technology expertise to post-acute care providers</h1>
  </section>

  <section class="block values-panel">
    <h2 class="label label-values">Our Core Values</h2>
    <ul class="list-values">
      <li>Client Focused</li>
      <li>Accountability</li>
      <li>Integrity</li>
      <li>Personal Development</li>
    </ul>
    <h2 class="label label-objectives">Our Primary Objectives</h2>
    <ul class="list-objectives">
      <li>Understand and exceed client expectations</li>
      <li>Committed to be a partner, not vendor</li>
      <li>Provide simplified change management expertise</li>
    </ul>
  </section>

  <section class="block services-panel">
    <h2 class="services-title">OUR<br>SERVICES</h2>
    <p class="services-intro">We understand different organizations have different needs.&nbsp; Brevalink Pro strives to assist your organization by bringing solutions that are easy to understand and allow the client to track success.&nbsp; We provide solutions based on the client’s needs and desires.</p>
    <h3 class="label">Information Technology</h3>
    <ul class="it-list">
      <li>CIO or IT Director Services</li>
      <li>CISO or Information Security Officer</li>
      <li>Comprehensive ePHI Risk Assessments</li>
      <li>IT Department Evaluation</li>
      <li>Policy Management and Consulting</li>
      <li>On-going IT department support</li>
    </ul>
  </section>

  <div class="block photo-medical" role="img" aria-label="Photo of a gloved hand with a stethoscope beside blue hexagon medical icons"></div>

  <section class="block mission-panel">
    <p class="statement statement-mission">Our Mission<br>Partner with clients to increase the value and security of their technology tools.</p>
    <p class="statement statement-goal">Our Goal<br>Become the premiere consulting company for Information Technology in the post-acute care industries.</p>
  </section>

  <div class="block photo-desk" role="img" aria-label="Photo of a doctor at a desk using a phone next to a laptop"></div>
</main>
</body>
</html>
```